Dating Coach For Women Seeks Professional CD Cover for Audio Series (and Long Walks on the Beach)

Believe it or not, I'm a dating coach for women.
In a few weeks, I'm launching a new coaching program called BLOOM Coaching (Brave, Lively, Open, Mindful). Yeah, it's a little cheesy, but the brand is upscale and professional. I work with smart, strong, successful women, 30-50, college educated, who are serious about understanding men and finding love.
I'm looking for a CD cover design (the actual CD, not the jewel case) and a matching newsletter to launch this BLOOM Coaching series.
Hopefully, you can provide a clean, professional feel that 'pops' using the same look and feel of my current brand. I'm looking for a design that builds off of the color scheme of my main website (red as a primary color) and my current products.
Please check out the site: http://www.tobiaslennhart.com/ as well as the below samples of my two products.
Where Did It Go eBook cover:
http://www.tobiaslennhart.com/images/where-did-it-go-small.png
Where Did It Go audio CD image:
http://www.tobiaslennhart.com/images/where-did-it-go-audio.jpg
Pairing Up in Pixels product spread
http://www.tobiaslennhart.com/images/TRL_ProductSpread-7cds.jpg
Pairing Up in Pixels audio CD
http://www.tobiaslennhart.com/images/cd3.jpg
The CD Cover probably won't have room for the full BLOOM acronym, but we'd like it somewhere on the newsletter. It will be a 4 page newsletter printed in full color, 11x17, folded to 8.5x11.
Any questions - just fire away. I want you to have all the information you need to succeed.
Many thanks and warmest wishes,
Tobias Ray Lennhart
Target Market(s)
college educated, professional, single women, 30-50 years old.
Industry/Entity Type
College
Look and feel

```html
<!DOCTYPE html>
<html lang="en">
<head>
<meta charset="UTF-8">
<title>BLOOM Coaching Newsletter Cover</title>
<link rel="stylesheet" href="https://fonts.googleapis.com/css2?family=Open+Sans:wght@300;400;700;800&display=swap">
<style>
  :root {
    --stage-bg: #d9ecf7;
    --band-black: #111111;
    --red-deep: #7a0c16;
    --red-main: #b3121f;
    --red-light: #d8303c;
    --white: #ffffff;
    --shirt-blue: #2f5f9e;
    --shirt-dark: #1c3a66;
  }
  * { box-sizing: border-box; margin: 0; padding: 0; }
  html, body {
    width: 1200px;
    height: 900px;
    overflow: hidden;
    background: var(--stage-bg);
    font-family: "Open Sans", Arial, sans-serif;
  }
  .stage {
    width: 1200px;
    height: 900px;
    display: flex;
    align-items: center;
    justify-content: center;
  }
  .cover {
    position: relative;
    width: 660px;
    height: 854px;
    overflow: hidden;
    background:
      radial-gradient(ellipse at 30% 35%, var(--red-light) 0%, var(--red-main) 45%, var(--red-deep) 100%);
    box-shadow: 0 10px 30px rgba(0,0,0,0.25);
    color: var(--white);
  }
  .top-band {
    height: 44px;
    background: var(--band-black);
    display: flex;
    align-items: center;
    padding-left: 26px;
    font-size: 19px;
    font-weight: 700;
    letter-spacing: 0.3px;
  }
  .masthead {
    position: absolute;
    left: 34px;
    top: 70px;
  }
  .masthead-title {
    font-size: 118px;
    font-weight: 800;
    line-height: 1;
    letter-spacing: -2px;
  }
  .masthead-sub {
    font-size: 66px;
    font-weight: 300;
    line-height: 1;
    margin-top: 4px;
    letter-spacing: 1px;
  }
  .coach-photo {
    position: absolute;
    right: 0;
    top: 250px;
    width: 330px;
    height: 400px;
    background:
      linear-gradient(180deg, rgba(179,18,31,0) 0%, rgba(47,95,158,0.9) 45%, var(--shirt-dark) 100%);
  }
  .traits {
    position: absolute;
    left: 40px;
    top: 312px;
    list-style: none;
  }
  .traits li {
    display: flex;
    align-items: center;
    font-size: 31px;
    font-weight: 400;
    line-height: 1.3;
  }
  .traits svg {
    width: 22px;
    height: 22px;
    margin-right: 12px;
  }
  .byline {
    position: absolute;
    left: 36px;
    top: 640px;
  }
  .byline-name {
    font-size: 60px;
    font-weight: 300;
    line-height: 1.05;
    letter-spacing: -0.5px;
  }
  .byline-tagline {
    font-size: 34px;
    font-weight: 700;
    line-height: 1.3;
  }
</style>
</head>
<body>
  <main class="stage">
    <article class="cover">
      <header class="top-band">Helping You On Your Journey To Love</header>

      <div class="masthead">
        <h1 class="masthead-title">BLOOM</h1>
        <div class="masthead-sub">COACHING</div>
      </div>

      <div class="coach-photo" role="img" aria-label="Portrait of the dating coach in a blue shirt, arms crossed, smiling"></div>

      <ul class="traits">
        <li><svg viewBox="0 0 24 24"><path d="M3 13 L9 19 L21 5" fill="none" stroke="var(--white)" stroke-width="4" stroke-linecap="round" stroke-linejoin="round"/></svg>Brave</li>
        <li><svg viewBox="0 0 24 24"><path d="M3 13 L9 19 L21 5" fill="none" stroke="var(--white)" stroke-width="4" stroke-linecap="round" stroke-linejoin="round"/></svg>Lively</li>
        <li><svg viewBox="0 0 24 24"><path d="M3 13 L9 19 L21 5" fill="none" stroke="var(--white)" stroke-width="4" stroke-linecap="round" stroke-linejoin="round"/></svg>Open</li>
        <li><svg viewBox="0 0 24 24"><path d="M3 13 L9 19 L21 5" fill="none" stroke="var(--white)" stroke-width="4" stroke-linecap="round" stroke-linejoin="round"/></svg>Mindful</li>
      </ul>

      <footer class="byline">
        <div class="byline-name">Tobias Ray Lennhart</div>
        <div class="byline-tagline">Your Personal Trainer for Love</div>
      </footer>
    </article>
  </main>
</body>
</html>
```